Velvet Lantern - listen to podcasts from around the world

http://randompodcasts.com/Velvet Lantern lets you listen to randomly selected podcasts from around the world. You can filter the podcasts by language. The power of randomness allows you to escape filter bubbles and echo chambers and discover issues and perspectives that you never knew existed. The current website offers basic functionality and is only a demo. Don't assume that anything in the current "design" should stay in place. The goal of the design should be to make it as easy as possible to understand what the app offers, to listen to new podcasts, and to skip to the next podcast. The service will be offered both as mobile apps and directly on the website. We expect that most users will be on mobile devices which is why we are focusing on the mobile/web app design.In addition to the current functionality, the app should also offer search (allowing the user to listen to podcasts that match given keywords), allow the user to easily subscribe to the current podcast and show the profile picture of the current podcast.

Target Market(s)

People interested in podcasts, all around the world

Colors

Designer to choose colors to be used in the design.

Requirements
Must have
• The main challenge is how to communicate the concept of the app to the user. Podcasts are randomly selected and the user just skips to the next one when he/she wants to. The ability to filter podcasts by language is important but no other filters are needed. The point is to use the power of random selection to explore new surprising content.
Nice to have
• The app/website is targeting a global audience. The less reliant the design is on written language, the better.

```html
<!DOCTYPE html>
<html lang="en">
<head>
<meta charset="utf-8">
<title>Velvet Lantern – App Screens</title>
<link href="https://fonts.googleapis.com/css2?family=Lato:wght@400;700&display=swap" rel="stylesheet">
<style>
  :root{
    --coral:#f45f4d;
    --stage:#1c1614;
    --screen:#f4f4f4;
    --white:#ffffff;
    --ink:#1f1f1f;
    --muted:#8a8a8a;
    --line:#e4e4e4;
    --star-off:#c9c9c9;
    --map:#e6e6e6;
  }
  *{box-sizing:border-box;margin:0;padding:0}
  html,body{width:1200px;height:1200px;overflow:hidden;background:var(--stage);font-family:'Lato',sans-serif;color:var(--ink)}
  .canvas{position:relative;width:1200px;height:1200px}
  .screen{position:absolute;width:247px;height:534px;background:var(--screen);border-radius:30px;overflow:hidden}
  .status{position:absolute;top:0;left:0;right:0;height:30px;font-size:11px;color:var(--muted)}
  .status .time{position:absolute;left:21px;top:10px}
  .status svg{position:absolute;right:14px;top:11px}
  .status.light{color:var(--white)}
  .home-bar{position:absolute;bottom:10px;left:50%;width:90px;height:3px;margin-left:-45px;border-radius:2px;background:#c4c4c4}
  .abs{position:absolute}
  .brand-dot{position:absolute;border-radius:50%;background:var(--coral)}
  .map-area{position:absolute;left:0;width:247px;background:radial-gradient(ellipse at center,var(--map) 0%,rgba(230,230,230,0) 72%)}
  .wordmark{position:absolute;left:0;right:0;text-align:center;color:var(--coral);font-weight:400;letter-spacing:.5px}
  .field{position:absolute;left:13px;width:221px;height:34px;background:var(--white);border:1px solid var(--line);border-radius:2px;font-size:10.5px;color:var(--muted);padding:11px 12px}
  .btn{position:absolute;left:35px;width:176px;height:34px;background:var(--coral);color:var(--white);font-weight:700;font-size:13px;text-align:center;line-height:34px;border-radius:2px}
  .header{position:absolute;left:0;right:0;top:0;background:var(--coral)}
  .header-title{position:absolute;left:0;right:0;top:42px;text-align:center;color:var(--white);font-size:12.5px;font-weight:700}
  .back{position:absolute;left:13px;top:42px}
  .section{position:absolute;left:8px;font-size:10px;color:var(--muted)}
  .row{position:absolute;left:8px;right:8px;height:34px;border-bottom:1px solid var(--line);font-size:10.5px;display:flex;align-items:center;justify-content:space-between;padding:0 6px 0 8px}
  .tabbar{position:absolute;left:0;right:0;bottom:0;height:60px;background:var(--white)}
  .tab{position:absolute;top:14px;font-size:8px;text-align:center;width:40px}
  .tab.active{color:var(--coral)}
</style>
</head>
<body>
<div class="canvas">

  <!-- Splash -->
  <section class="screen splash" style="left:59px;top:33px">
    <div class="status"><span class="time">9:41</span>
      <svg width="44" height="8" viewBox="0 0 44 8"><rect x="0" y="5" width="2" height="3" fill="#8a8a8a"/><rect x="3" y="3" width="2" height="5" fill="#8a8a8a"/><rect x="6" y="1" width="2" height="7" fill="#8a8a8a"/><path d="M14 3a6 6 0 0 1 8 0M16 5a3 3 0 0 1 4 0" stroke="#8a8a8a" fill="none"/><rect x="29" y="1" width="14" height="6" rx="1" fill="#8a8a8a"/></svg>
    </div>
    <div class="map-area" role="img" aria-label="Dotted world map in light grey" style="top:136px;height:240px"></div>
    <div class="brand-dot" style="left:87px;top:237px;width:72px;height:72px"></div>
    <div class="wordmark" style="top:322px;font-size:15px">VELVET LANTERN</div>
    <div class="home-bar"></div>
  </section>

  <!-- Login -->
  <section class="screen login" style="left:383px;top:33px">
    <div class="status"><span class="time">9:41</span>
      <svg width="44" height="8" viewBox="0 0 44 8"><rect x="0" y="5" width="2" height="3" fill="#8a8a8a"/><rect x="3" y="3" width="2" height="5" fill="#8a8a8a"/><rect x="6" y="1" width="2" height="7" fill="#8a8a8a"/><path d="M14 3a6 6 0 0 1 8 0M16 5a3 3 0 0 1 4 0" stroke="#8a8a8a" fill="none"/><rect x="29" y="1" width="14" height="6" rx="1" fill="#8a8a8a"/></svg>
    </div>
    <div class="map-area" role="img" aria-label="Dotted world map in light grey" style="top:136px;height:240px"></div>
    <div class="brand-dot" style="left:97px;top:94px;width:48px;height:48px"></div>
    <div class="wordmark" style="top:150px;font-size:11px">VELVET LANTERN</div>
    <div class="abs" style="left:0;right:0;top:185px;text-align:center;font-size:15px;letter-spacing:.5px">LOGIN</div>
    <div class="field" style="top:218px">Email</div>
    <div class="field" style="top:261px">Password</div>
    <div class="abs" style="right:13px;top:303px;font-size:10.5px">Forgot Password?</div>
    <div class="btn" style="top:337px">Let’s Start</div>
    <div class="abs" style="left:0;right:0;top:465px;text-align:center;font-size:10px">Don’t have an account yet? <span style="color:var(--coral)">Signup</span></div>
    <div class="home-bar"></div>
  </section>

  <!-- Logo display -->
  <div class="brand-dot" style="left:876px;top:244px;width:160px;height:160px"></div>
  <div class="abs" style="left:780px;width:352px;top:432px;text-align:center;color:var(--coral);font-size:33px;letter-spacing:.5px">VELVET LANTERN</div>

  <!-- Forgot password -->
  <section class="screen forgot" style="left:307px;top:631px">
    <div class="header" style="height:179px"></div>
    <div class="status light"><span class="time">9:41</span>
      <svg width="44" height="8" viewBox="0 0 44 8"><rect x="0" y="5" width="2" height="3" fill="#fff"/><rect x="3" y="3" width="2" height="5" fill="#fff"/><rect x="6" y="1" width="2" height="7" fill="#fff"/><path d="M14 3a6 6 0 0 1 8 0M16 5a3 3 0 0 1 4 0" stroke="#fff" fill="none"/><rect x="29" y="1" width="14" height="6" rx="1" fill="#fff"/></svg>
    </div>
    <svg class="back" width="10" height="16" viewBox="0 0 10 16"><path d="M8 1 2 8l6 7" stroke="#fff" stroke-width="1.6" fill="none"/></svg>
    <div class="header-title">Forgot Password</div>
    <svg class="abs" style="left:96px;top:96px" width="54" height="54" viewBox="0 0 54 54"><circle cx="38" cy="16" r="13" fill="#fff"/><circle cx="40" cy="13" r="4" fill="#f45f4d"/><path d="M29 24 5 44l4 4 4-3 3 3 4-4-3-3 4-3" fill="#fff"/><path d="M28 22 4 43l5 6 20-17" fill="#fff"/></svg>
    <div class="abs" style="left:0;right:0;top:200px;text-align:center;font-size:15px">Did you forget your pasword?</div>
    <p class="abs" style="left:14px;right:14px;top:234px;text-align:center;font-size:8.3px;line-height:11px">If you have forgotten your password, enter the email address associated with your account into the box below and we will send you instructions on how to reset your password to your email account.</p>
    <div class="field" style="top:292px">Email Address</div>
    <div class="btn" style="top:341px">Reset</div>
    <div class="home-bar"></div>
  </section>

  <!-- Language list -->
  <section class="screen languages" style="left:626px;top:631px">
    <div class="header" style="height:90px"></div>
    <div class="status light"><span class="time">9:41</span>
      <svg width="44" height="8" viewBox="0 0 44 8"><rect x="0" y="5" width="2" height="3" fill="#fff"/><rect x="3" y="3" width="2" height="5" fill="#fff"/><rect x="6" y="1" width="2" height="7" fill="#fff"/><path d="M14 3a6 6 0 0 1 8 0M16 5a3 3 0 0 1 4 0" stroke="#fff" fill="none"/><rect x="29" y="1" width="14" height="6" rx="1" fill="#fff"/></svg>
    </div>
    <svg class="back" width="10" height="16" viewBox="0 0 10 16"><path d="M8 1 2 8l6 7" stroke="#fff" stroke-width="1.6" fill="none"/></svg>
    <div class="header-title">Velvet Lantern</div>
    <div class="abs" style="left:8px;right:9px;top:70px;height:36px;background:var(--white);border-radius:2px;box-shadow:0 1px 3px rgba(0,0,0,.08);font-size:10.5px;color:var(--muted);padding:12px 0 0 42px">Search here
      <svg class="abs" style="left:16px;top:11px" width="14" height="14" viewBox="0 0 14 14"><circle cx="6" cy="6" r="4.5" stroke="#8a8a8a" stroke-width="1.3" fill="none"/><path d="m9.5 9.5 3.5 3.5" stroke="#8a8a8a" stroke-width="1.3"/></svg>
    </div>
    <div class="section" style="top:125px">Favourite</div>
    <div class="row" style="top:137px">English (10850)<svg width="13" height="13" viewBox="0 0 24 24"><path d="m12 2 3 7 7 .6-5.4 4.7 1.7 7.2L12 17.8 5.7 21.5l1.7-7.2L2 9.6 9 9z" fill="#f45f4d"/></svg></div>
    <div class="row" style="top:171px">中文 / Chinese (271)<svg width="13" height="13" viewBox="0 0 24 24"><path d="m12 2 3 7 7 .6-5.4 4.7 1.7 7.2L12 17.8 5.7 21.5l1.7-7.2L2 9.6 9 9z" fill="#f45f4d"/></svg></div>
    <div class="section" style="top:226px">All Language</div>
    <div class="row" style="top:239px">español / Spanish (914)<svg width="13" height="13" viewBox="0 0 24 24"><path d="m12 2 3 7 7 .6-5.4 4.7 1.7 7.2L12 17.8 5.7 21.5l1.7-7.2L2 9.6 9 9z" fill="#c9c9c9"/></svg></div>
    <div class="row" style="top:273px">français / French (860)<svg width="13" height="13" viewBox="0 0 24 24"><path d="m12 2 3 7 7 .6-5.4 4.7 1.7 7.2L12 17.8 5.7 21.5l1.7-7.2L2 9.6 9 9z" fill="#c9c9c9"/></svg></div>
    <div class="row" style="top:308px">português / Portuguese (344)<svg width="13" height="13" viewBox="0 0 24 24"><path d="m12 2 3 7 7 .6-5.4 4.7 1.7 7.2L12 17.8 5.7 21.5l1.7-7.2L2 9.6 9 9z" fill="#c9c9c9"/></svg></div>
    <div class="row" style="top:342px">svenska / Swedish (313)<svg width="13" height="13" viewBox="0 0 24 24"><path d="m12 2 3 7 7 .6-5.4 4.7 1.7 7.2L12 17.8 5.7 21.5l1.7-7.2L2 9.6 9 9z" fill="#c9c9c9"/></svg></div>
    <div class="row" style="top:377px">norsk / Norwegian (132)<svg width="13" height="13" viewBox="0 0 24 24"><path d="m12 2 3 7 7 .6-5.4 4.7 1.7 7.2L12 17.8 5.7 21.5l1.7-7.2L2 9.6 9 9z" fill="#c9c9c9"/></svg></div>
    <div class="row" style="top:411px">čeština / Czech (65)<svg width="13" height="13" viewBox="0 0 24 24"><path d="m12 2 3 7 7 .6-5.4 4.7 1.7 7.2L12 17.8 5.7 21.5l1.7-7.2L2 9.6 9 9z" fill="#c9c9c9"/></svg></div>
    <div class="row" style="top:446px">slovenščina / Slovenian (58)<svg width="13" height="13" viewBox="0 0 24 24"><path d="m12 2 3 7 7 .6-5.4 4.7 1.7 7.2L12 17.8 5.7 21.5l1.7-7.2L2 9.6 9 9z" fill="#c9c9c9"/></svg></div>
    <nav class="tabbar">
      <div class="tab active" style="left:20px">
        <svg width="18" height="14" viewBox="0 0 18 14"><path d="M1 1h16M1 7h16M1 13h16" stroke="#f45f4d" stroke-width="1.8"/></svg><br>List
      </div>
      <div class="tab" style="left:185px">
        <svg width="16" height="16" viewBox="0 0 16 16"><circle cx="8" cy="5" r="3.5" stroke="#555" stroke-width="1.3" fill="none"/><path d="M1.5 15.5a6.5 6.5 0 0 1 13 0" stroke="#555" stroke-width="1.3" fill="none"/></svg><br>Profile
      </div>
    </nav>
    <div class="brand-dot" style="left:96px;top:464px;width:52px;height:52px;box-shadow:0 3px 8px rgba(244,95,77,.4)">
      <svg class="abs" style="left:20px;top:17px" width="15" height="18" viewBox="0 0 15 18"><path d="M1 1l13 8-13 8z" fill="#fff"/></svg>
    </div>
    <div class="home-bar" style="background:#aaa"></div>
  </section>

</div>
</body>
</html>
```